Need Landing Page for Data Security Company

Need a new landing page (PSD) for our data security company (www.korvadel.com). We specialize in selling patented hard drive destruction machines that guarantee the data on your hard drives are unrecoverable. We have several large clients such as Lumigrove, Chirpaloo and Vendrix just to name a few. Really want to have a landing page that sticks out.

Attached is a one pager we use just for emailing clients. We do not want the landing page to look like this. This is just for content to read. The landing page needs

Target Market(s)

Government, business corporations, IT decision makers. Not every day user

Industry/Entity Type

It Company

Number of Pages Required

1 page

Font styles to use
Other font styles liked:
• Match Current Website

Requirements
Must have
• Its a landing page so it needs a Contact us Section at the very top!!!
• Need to be a very attractive landing page.. Would like a mix of showcasing our products and also having some client list to show our bigger name clients (lumigrove, vendrix, chirpaloo)
• Landing page needs to use the same color/style schema as current website. Also will be using the same menu structure as what exists today.
• www.korvadel.com
Nice to have
• Maybe some streamvault videos of our products?

```html
<!DOCTYPE html>
<html lang="en">
<head>
<meta charset="utf-8">
<title>Korvadel Technologies</title>
<link rel="stylesheet" href="https://fonts.googleapis.com/css2?family=Raleway:wght@400;600;700;800&family=Open+Sans:wght@400;600;700&display=swap">
<style>
:root{
  --green:#6cb33f;
  --green-dark:#3f8a1e;
  --ink:#333;
  --muted:#8a8a8a;
  --footer:#2a2a2a;
  --footer-bottom:#1e1e1e;
  --white:#fff;
}
*{box-sizing:border-box;margin:0;padding:0}
html,body{width:1200px;height:2696px;overflow:hidden;background:var(--white)}
body{position:relative;font-family:"Open Sans",Arial,sans-serif;color:var(--ink)}
.abs{position:absolute}

.site-header{left:0;top:0;width:1200px;height:96px;background:var(--white)}
.brand{left:196px;top:26px;display:flex;align-items:center;gap:10px}
.brand-mark{width:38px;height:38px;border-radius:50%;background:var(--green)}
.brand-name{font-family:"Raleway",sans-serif;font-weight:700;font-size:34px;color:#222;letter-spacing:.5px}
.brand-tag{font-size:9px;color:var(--muted);letter-spacing:1px;margin-top:-2px}
.call{right:196px;top:22px;text-align:right}
.call small{display:block;font-size:14px;color:var(--muted)}
.call strong{display:flex;align-items:center;gap:8px;font-family:"Raleway",sans-serif;font-size:24px;color:#222}

.main-nav{left:0;top:96px;width:1200px;height:36px;background:var(--green);display:flex;justify-content:center}
.main-nav ul{display:flex;list-style:none;width:808px}
.main-nav li{font-family:"Raleway",sans-serif;font-weight:700;font-size:13px;color:var(--white);padding:0 26px;line-height:36px;text-transform:uppercase}
.main-nav li.active{background:var(--green-dark)}

.hero{left:0;top:132px;width:1200px;height:600px;background:linear-gradient(180deg,#6f7780 0%,#9aa1a8 45%,#c9ccd0 100%)}
.hero-title{left:0;top:270px;width:1200px;text-align:center;font-family:"Raleway",sans-serif;font-weight:800;font-size:44px;color:var(--white);letter-spacing:1px;text-shadow:0 2px 6px rgba(0,0,0,.4)}
.hero-sub{left:0;top:330px;width:1200px;text-align:center;font-family:"Raleway",sans-serif;font-weight:700;font-size:22px;color:var(--white);letter-spacing:2px;text-shadow:0 2px 4px rgba(0,0,0,.4)}

.feature{top:600px;width:250px;height:250px;background:var(--green);color:var(--white);text-align:center;padding:88px 24px 0}
.feature.mid{top:576px;height:298px;background:var(--green-dark);padding-top:112px}
.feature-thumb{position:absolute;left:50%;top:-50px;width:120px;height:120px;margin-left:-60px;border-radius:50%;border:5px solid var(--white);background:radial-gradient(circle,#c8ccd0,#6e747a)}
.feature.mid .feature-thumb{top:-26px}
.feature h3{font-family:"Raleway",sans-serif;font-weight:800;font-size:17px;line-height:1.2;text-transform:uppercase}
.feature p{font-size:11px;line-height:1.5;margin-top:10px;opacity:.9}
.btn{display:inline-block;margin-top:16px;font-family:"Raleway",sans-serif;font-weight:700;font-size:11px;padding:7px 16px;background:var(--white);color:var(--green-dark);text-transform:uppercase}

.section-title{left:0;width:1200px;text-align:center;font-family:"Raleway",sans-serif;font-weight:700;font-size:30px;color:#333}
.section-title.green{color:var(--green)}
.about-text{left:230px;width:740px;text-align:center;font-size:12px;line-height:1.7;color:var(--muted)}

.products-band{left:0;top:1240px;width:1200px;height:740px;background:linear-gradient(180deg,#fff 0%,#f3f3f3 45%,#e6e7e8 100%)}
.product{width:360px}
.product-photo{width:360px;height:184px;background:linear-gradient(135deg,#5d8f62,#a9b1a3 55%,#dfe2df);position:relative}
.play{position:absolute;left:50%;top:50%;width:40px;height:40px;margin:-20px 0 0 -20px;border-radius:50%;background:var(--white)}
.play::after{content:"";position:absolute;left:16px;top:12px;border-left:12px solid #333;border-top:8px solid transparent;border-bottom:8px solid transparent}
.product h4{font-family:"Raleway",sans-serif;font-weight:600;font-size:26px;color:var(--green);margin-top:10px}
.product p{font-size:11px;line-height:1.6;color:var(--muted);margin-top:4px}
.arrow{top:1366px;width:20px;height:60px}

.clients{left:210px;top:2150px;width:780px;display:grid;grid-template-columns:repeat(7,1fr);row-gap:26px;column-gap:12px}
.client{display:flex;align-items:center;justify-content:center;gap:6px;font-weight:700;font-size:12px;color:#444}
.client i{display:block;width:12px;height:12px;background:#444}

.site-footer{left:0;top:2380px;width:1200px;height:316px;background:var(--footer)}
.footer-col{top:2418px;color:#cfcfcf;font-size:12px;line-height:1.9}
.footer-col h5{font-family:"Raleway",sans-serif;font-weight:600;font-size:20px;color:var(--white);margin-bottom:6px}
.footer-bottom{left:0;top:2656px;width:1200px;height:40px;background:var(--footer-bottom);color:#777;font-size:10px;line-height:40px;padding-left:208px}
</style>
</head>
<body>

<header class="site-header abs">
  <div class="brand abs">
    <span class="brand-mark"></span>
    <div>
      <div class="brand-name">Korvadel</div>
      <div class="brand-tag">DATA DESTRUCTION SYSTEMS</div>
    </div>
  </div>
  <div class="call abs">
    <small>Call Us Now</small>
    <strong>
      <svg width="18" height="18" viewBox="0 0 24 24"><path d="M6.6 10.8a15.1 15.1 0 0 0 6.6 6.6l2.2-2.2c.3-.3.7-.4 1-.2 1.1.4 2.3.6 3.6.6.6 0 1 .4 1 1V20c0 .6-.4 1-1 1A17 17 0 0 1 3 4c0-.6.4-1 1-1h3.5c.6 0 1 .4 1 1 0 1.2.2 2.4.6 3.6.1.3 0 .7-.2 1z" fill="#6cb33f"/></svg>
      555-014-2290
    </strong>
  </div>
</header>

<nav class="main-nav abs">
  <ul>
    <li>Home</li><li class="active">About Us</li><li>Products</li><li>Services</li><li>Compliance</li><li>Blog</li><li>Contact</li>
  </ul>
</nav>

<section class="hero abs" role="img" aria-label="Close-up photograph of opened hard drives and server hardware"></section>
<h1 class="hero-title abs">KORVADEL INNOVATIVE SOLUTIONS</h1>
<p class="hero-sub abs">THE ONLY HASSLE FREE AUTOMATED SHREDDING SYSTEM</p>

<article class="feature abs" style="left:230px">
  <div class="feature-thumb" role="img" aria-label="Hard drive platter photograph"></div>
  <h3>Computer<br>Storage Media</h3>
  <p>Drives, tapes and flash media hold sensitive records that must be fully destroyed.</p>
  <span class="btn">Read More</span>
</article>
<article class="feature mid abs" style="left:475px">
  <div class="feature-thumb" role="img" aria-label="Destroyer machine photograph"></div>
  <h3>Korvadel DiskClamp<br>Destroyer</h3>
  <p>Our patented machine bends and punctures every drive so data cannot be recovered.</p>
  <span class="btn">Read More</span>
</article>
<article class="feature abs" style="left:720px">
  <div class="feature-thumb" role="img" aria-label="Crushed hard drive parts photograph"></div>
  <h3>Crushed, Mangled<br>and Shredded</h3>
  <p>Each destroyed device leaves no readable surface, meeting strict compliance rules.</p>
  <span class="btn">Read More</span>
</article>

<h2 class="section-title abs" style="top:936px">ABOUT KORVADEL TECHNOLOGIES</h2>
<p class="about-text abs" style="top:988px">Korvadel Technologies, Inc. is a data destruction technology research and development company dedicated to engineering secure disposal solutions for government, business and information technology teams across the country.</p>
<p class="about-text abs" style="top:1040px">Our company is a trusted name for destroying hard drives and storage media. Our patented machines are used daily by agencies, banks and hospitals that need proof that retired data is gone for good and that every audit can be passed with confidence.</p>

<div class="products-band abs" role="img" aria-label="Faint background photograph of circuit boards"></div>
<h2 class="section-title green abs" style="top:1160px">KORVADEL PRODUCTS</h2>

<svg class="arrow abs" style="left:150px" viewBox="0 0 20 60"><path d="M18 2 2 30l16 28" fill="none" stroke="#bbb" stroke-width="2"/></svg>
<svg class="arrow abs" style="left:1030px" viewBox="0 0 20 60"><path d="M2 2l16 28L2 58" fill="none" stroke="#bbb" stroke-width="2"/></svg>

<article class="product abs" style="left:232px;top:1308px">
  <div class="product-photo" role="img" aria-label="Video still of the DiskClamp machine"><span class="play"></span></div>
  <h4>DiskClamp</h4>
  <p>A compact desktop unit that bends and pierces hard drives in seconds. Quiet, safe and built for offices that destroy media every day.</p>
</article>
<article class="product abs" style="left:620px;top:1308px">
  <div class="product-photo" role="img" aria-label="Video still of the DiskClamp Compact machine"><span class="play"></span></div>
  <h4>DiskClamp Compact</h4>
  <p>The smaller model for laptop drives and tight spaces. Same proven force in a lighter frame that fits on any shelf or cart.</p>
</article>
<article class="product abs" style="left:232px;top:1708px">
  <div class="product-photo" role="img" aria-label="Video still of the DiskDice machine"><span class="play"></span></div>
  <h4>DiskDice</h4>
  <p>Cuts storage media into small pieces for full compliance. Ideal for large teams that handle high volumes of retired equipment.</p>
</article>
<article class="product abs" style="left:620px;top:1708px">
  <div class="product-photo" role="img" aria-label="Video still of the DiskClamp SSD machine"><span class="play"></span></div>
  <h4>DiskClamp SSD</h4>
  <p>Built for solid state drives and chips. Breaks every memory cell so nothing can be read back, meeting the latest guidelines.</p>
</article>

<h2 class="section-title abs" style="top:2080px;font-weight:400">Our Clients</h2>
<div class="clients abs">
  <span class="client">Oxtera</span><span class="client">Belcana</span><span class="client">Quorvix</span><span class="client">Tarnfield</span><span class="client">Halvex</span><span class="client">Merrow</span><span class="client"><i></i>Sundale</span>
  <span class="client">Vendrix</span><span class="client">Chirpaloo</span><span class="client">Pellory</span><span class="client">Crestmark</span><span class="client">Ovanta</span><span class="client">streamvault</span><span class="client">Lumigrove</span>
</div>

<footer class="site-footer abs"></footer>
<div class="footer-col abs" style="left:208px">
  <h5>Quick Links</h5>Home<br>About Us<br>Our Clients<br>Services
</div>
<div class="footer-col abs" style="left:372px">
  <h5>Products</h5>DiskClamp<br>DiskClamp Compact<br>DiskDice<br>DiskClamp SSD
</div>
<div class="footer-col abs" style="left:548px">
  <h5>Resources</h5>DiskClamp Compact SSD<br>DiskClamp SSD Tower<br>DiskClamp Rackmount
</div>
<div class="footer-col abs" style="left:748px">
  <h5>Contact Info</h5>48 Larkspur Way, Unit 3, Brindle Bay, FL 00000<br>Office: 555-014-2290<br>Fax: 555-014-2291<br>Email: info@korvadel.com
</div>
<div class="footer-bottom abs">© Korvadel Technologies. All rights reserved. Terms of use.</div>

</body>
</html>
```